2022 Landscaping Services

Please use the prior year design as an example. Similar style but DO NOT COPY IT EXACTLY- you can use different photos from our website if you like. Same text for year 2022.
Design should clearly depict the differences between the 3 products so people can buy one of them. Be creative!

size 8.5" x 11"

Must provide source file in photoshop if you are winner

Requirements
Must have
• Same text as original flier but with year 2022

```html
<!DOCTYPE html>
<html lang="en">
<head>
<meta charset="utf-8">
<title>2022 Gravesite Landscaping Packages</title>
<link href="https://fonts.googleapis.com/css2?family=Fira+Sans:wght@400;500;600;700;800&family=Pacifico&display=swap" rel="stylesheet">
<style>
  :root {
    --red: #8c1c22;
    --red-deep: #7f161c;
    --rose: #d8a497;
    --rose-line: #e2b8ae;
    --ink: #3a3a3c;
    --grey: #4b4c4f;
    --paper: #ffffff;
    --backdrop: #ecebe8;
    --badge: #3b63b8;
  }
  * { box-sizing: border-box; margin: 0; padding: 0; }
  html, body { width: 1200px; height: 848px; overflow: hidden; }
  body { background: var(--backdrop); font-family: "Fira Sans", Arial, sans-serif; color: var(--ink); }

  .flyer {
    position: absolute; left: 283px; top: 14px;
    width: 634px; height: 820px; background: var(--paper);
    box-shadow: 0 4px 18px rgba(0,0,0,.18);
    overflow: hidden;
  }

  .hero-frame {
    position: absolute; left: 242px; top: 0; width: 392px; height: 352px;
    background: var(--red);
  }
  .hero-photo {
    position: absolute; left: 232px; top: 10px; width: 388px; height: 342px;
    border-bottom-left-radius: 95px;
    background:
      linear-gradient(180deg, #e9ede6 0%, #7f9c5a 12%, #4e6e34 38%, #6f8a4c 55%, #c9ccc4 66%, #a9aca6 78%, #8fb05a 88%, #6d8f3e 100%);
  }

  .brand {
    position: absolute; left: 20px; top: 34px; width: 200px;
    display: flex; flex-direction: column; align-items: center; gap: 12px;
  }
  .brand-mark { width: 76px; height: 76px; border-radius: 50%; border: 2px solid var(--red); }
  .brand-name {
    font-weight: 600; font-size: 19px; line-height: 1.2; color: var(--red);
    text-align: center; text-transform: uppercase; letter-spacing: .5px; white-space: nowrap;
  }

  .title { position: absolute; left: 38px; top: 236px; line-height: .95; }
  .title-year { font-size: 40px; font-weight: 800; color: var(--red); }
  .title-line1 { font-size: 34px; font-weight: 500; color: var(--grey); }
  .title-line2 { font-size: 27px; font-weight: 500; color: var(--red); margin-top: 2px; }
  .title-line3 { font-size: 34px; font-weight: 800; color: var(--grey); margin-top: 2px; }

  .badge {
    position: absolute; left: 545px; top: 340px; width: 56px; height: 56px;
    border-radius: 50%; background: var(--badge); border: 2px solid #fff;
    color: #fff; font-family: "Pacifico", cursive; font-size: 11px; line-height: 1.05;
    display: flex; align-items: center; justify-content: center; text-align: center;
    z-index: 3;
  }

  .packages {
    position: absolute; left: 44px; top: 398px; width: 548px;
    border-collapse: collapse; table-layout: fixed;
  }
  .packages td, .packages th { border: 1px solid var(--rose-line); vertical-align: middle; }
  .packages col { width: 137px; }

  .head th { height: 50px; text-align: left; padding: 6px 8px; font-weight: 700; text-transform: uppercase; line-height: 1; }
  .head .label { color: var(--red); font-size: 15px; }
  .pkg-name { font-size: 15px; display: block; }
  .pkg-sub { font-size: 12px; display: block; margin-top: 2px; }
  .col-seasonal { background: var(--paper); color: var(--red); }
  .col-basic { background: var(--rose); color: var(--red); }
  .col-perpetual { background: var(--red-deep); color: #fff; }

  .intro-row td { height: 44px; }
  .service { font-size: 10px; font-weight: 500; text-transform: uppercase; padding: 4px 8px; line-height: 1.2; color: var(--ink); }
  .note { font-size: 7.6px; text-align: center; padding: 3px 5px; line-height: 1.25; }
  .col-perpetual.note, .col-perpetual .price-sub { color: #fff; }
  .cell { height: 34px; text-align: center; }
  .cell svg { display: inline-block; vertical-align: middle; }
  .col-perpetual.cell { border-color: #a8454b; }

  .price-row td { height: 44px; text-align: center; }
  .price { font-size: 17px; font-weight: 700; color: var(--red); line-height: 1; }
  .col-perpetual .price { color: #fff; }
  .price-sub { font-size: 7.5px; display: block; color: var(--ink); }
  .price-trio { display: flex; justify-content: center; gap: 4px; align-items: flex-start; }
  .price-trio .bar { font-size: 16px; font-weight: 700; color: var(--red); line-height: 1; }
  .price-trio .price { font-size: 15px; }

  .valid-row td { height: 42px; }
  .valid { font-size: 10px; font-weight: 500; padding: 4px 8px; line-height: 1.2; }

  .footer {
    position: absolute; left: 44px; top: 790px; width: 548px; height: 24px;
    background: var(--red); color: #fff; font-weight: 600; font-size: 12.5px;
    display: flex; align-items: center; justify-content: center;
  }
</style>
</head>
<body>
<main class="flyer">
  <div class="hero-frame"></div>
  <div class="hero-photo" role="img" aria-label="Photo of a tree-lined cemetery drive with rows of headstones and trimmed shrubs"></div>

  <div class="brand">
    <span class="brand-mark"></span>
    <span class="brand-name">Elmwood Hollow<br>Cemetery</span>
  </div>

  <h1 class="title">
    <div class="title-year">2022</div>
    <div class="title-line1">GRAVESITE</div>
    <div class="title-line2">LANDSCAPING</div>
    <div class="title-line3">PACKAGES</div>
  </h1>

  <div class="badge">Most<br>Popular</div>

  <table class="packages">
    <colgroup><col><col><col><col></colgroup>
    <tr class="head">
      <th class="label">Services<br>Offered</th>
      <th class="col-seasonal"><span class="pkg-name">Seasonal</span><span class="pkg-sub">Care Endowment</span></th>
      <th class="col-basic"><span class="pkg-name">Basic</span><span class="pkg-sub">Care Endowment</span></th>
      <th class="col-perpetual"><span class="pkg-name">Perpetual</span><span class="pkg-sub">Care Endowment</span></th>
    </tr>
    <tr class="intro-row">
      <td class="service">Weeding &amp; Trimming on Your Gravesite</td>
      <td class="note col-seasonal" style="color:var(--ink)">Approximately every 7 weeks during the growing season: Mid-April through Mid-October</td>
      <td class="note col-basic" style="color:var(--ink)">2 times per year:<br>Mid-May &amp; Mid-September</td>
      <td class="note col-perpetual">Approximately every 7 weeks during the growing season: Mid-April through Mid-October</td>
    </tr>
    <tr>
      <td class="service">Payment Ensured Forever Grave Care</td>
      <td class="cell col-seasonal"><svg width="14" height="14" viewBox="0 0 14 14"><circle cx="7" cy="7" r="5.5" fill="none" stroke="#8c1c22" stroke-width="1.6"/><line x1="3.2" y1="3.2" x2="10.8" y2="10.8" stroke="#8c1c22" stroke-width="1.6"/></svg></td>
      <td class="cell col-basic"><svg width="14" height="14" viewBox="0 0 14 14"><path d="M2 7.5 L5.5 11 L12 2.5" fill="none" stroke="#8c1c22" stroke-width="1.4"/></svg></td>
      <td class="cell col-perpetual"><svg width="14" height="14" viewBox="0 0 14 14"><path d="M2 7.5 L5.5 11 L12 2.5" fill="none" stroke="#fff" stroke-width="1.4"/></svg></td>
    </tr>
    <tr>
      <td class="service">Momument Leveling</td>
      <td class="cell col-seasonal"><svg width="14" height="14" viewBox="0 0 14 14"><circle cx="7" cy="7" r="5.5" fill="none" stroke="#8c1c22" stroke-width="1.6"/><line x1="3.2" y1="3.2" x2="10.8" y2="10.8" stroke="#8c1c22" stroke-width="1.6"/></svg></td>
      <td class="cell col-basic"><svg width="14" height="14" viewBox="0 0 14 14"><path d="M2 7.5 L5.5 11 L12 2.5" fill="none" stroke="#8c1c22" stroke-width="1.4"/></svg></td>
      <td class="cell col-perpetual"><svg width="14" height="14" viewBox="0 0 14 14"><path d="M2 7.5 L5.5 11 L12 2.5" fill="none" stroke="#fff" stroke-width="1.4"/></svg></td>
    </tr>
    <tr>
      <td class="service">Monument Cleaning</td>
      <td class="cell col-seasonal"><svg width="14" height="14" viewBox="0 0 14 14"><circle cx="7" cy="7" r="5.5" fill="none" stroke="#8c1c22" stroke-width="1.6"/><line x1="3.2" y1="3.2" x2="10.8" y2="10.8" stroke="#8c1c22" stroke-width="1.6"/></svg></td>
      <td class="cell col-basic"><svg width="14" height="14" viewBox="0 0 14 14"><circle cx="7" cy="7" r="5.5" fill="none" stroke="#8c1c22" stroke-width="1.6"/><line x1="3.2" y1="3.2" x2="10.8" y2="10.8" stroke="#8c1c22" stroke-width="1.6"/></svg></td>
      <td class="cell col-perpetual"><svg width="14" height="14" viewBox="0 0 14 14"><path d="M2 7.5 L5.5 11 L12 2.5" fill="none" stroke="#fff" stroke-width="1.4"/></svg></td>
    </tr>
    <tr>
      <td class="service">Full Bed of Boxwood Shrubs</td>
      <td class="cell col-seasonal"><svg width="14" height="14" viewBox="0 0 14 14"><circle cx="7" cy="7" r="5.5" fill="none" stroke="#8c1c22" stroke-width="1.6"/><line x1="3.2" y1="3.2" x2="10.8" y2="10.8" stroke="#8c1c22" stroke-width="1.6"/></svg></td>
      <td class="cell col-basic"><svg width="14" height="14" viewBox="0 0 14 14"><circle cx="7" cy="7" r="5.5" fill="none" stroke="#8c1c22" stroke-width="1.6"/><line x1="3.2" y1="3.2" x2="10.8" y2="10.8" stroke="#8c1c22" stroke-width="1.6"/></svg></td>
      <td class="cell col-perpetual"><svg width="14" height="14" viewBox="0 0 14 14"><path d="M2 7.5 L5.5 11 L12 2.5" fill="none" stroke="#fff" stroke-width="1.4"/></svg></td>
    </tr>
    <tr>
      <td class="service">Replacement of Shrubs</td>
      <td class="cell col-seasonal"><svg width="14" height="14" viewBox="0 0 14 14"><circle cx="7" cy="7" r="5.5" fill="none" stroke="#8c1c22" stroke-width="1.6"/><line x1="3.2" y1="3.2" x2="10.8" y2="10.8" stroke="#8c1c22" stroke-width="1.6"/></svg></td>
      <td class="cell col-basic"><svg width="14" height="14" viewBox="0 0 14 14"><circle cx="7" cy="7" r="5.5" fill="none" stroke="#8c1c22" stroke-width="1.6"/><line x1="3.2" y1="3.2" x2="10.8" y2="10.8" stroke="#8c1c22" stroke-width="1.6"/></svg></td>
      <td class="cell col-perpetual"><svg width="14" height="14" viewBox="0 0 14 14"><path d="M2 7.5 L5.5 11 L12 2.5" fill="none" stroke="#fff" stroke-width="1.4"/></svg></td>
    </tr>
    <tr class="price-row">
      <td class="service" style="text-align:left">Trust Certificate</td>
      <td class="col-seasonal">
        <div class="price-trio">
          <span><span class="price">$357</span><span class="price-sub">3 years</span></span>
          <span class="bar">|</span>
          <span><span class="price">$238</span><span class="price-sub">2 years</span></span>
          <span class="bar">|</span>
          <span><span class="price">$119</span><span class="price-sub">1 year</span></span>
        </div>
      </td>
      <td class="col-basic"><span class="price">$255</span><span class="price-sub">12 Monthly payments</span></td>
      <td class="col-perpetual"><span class="price">$313</span><span class="price-sub">12 Monthly payments</span></td>
    </tr>
    <tr class="valid-row">
      <td class="valid">Valid through<br>10/31/22</td>
      <td class="note col-seasonal" style="color:var(--ink)">Multi-year payment locks<br>in current rate</td>
      <td class="note col-basic" style="color:var(--ink)">Call for single payment<br>discounts</td>
      <td class="note col-perpetual">Call for single payment<br>discounts</td>
    </tr>
  </table>

  <footer class="footer">48 Orchard Lane, Fairhaven NJ 07000 | (201) 555-0148 | elmwoodhollow.org</footer>
</main>
</body>
</html>
```